Business card for Eyelash extension salon in Beverly Hills,California USA

We need new business card for our salon in Beverly Hills. The salon name is 'Lumarra' . We would like to have...Business name: Lumarra Name of person: will provide later Address 6128 N.Corbel Ridge Blvd Beverly Hills , CA 90210 Phone: will provide later (Text only) Web: www.lumarrastudio-example.com Pictogrid icon, Friendvale icon follow us for seasonal campaign and news @lumarrastudioexample Design should look elegant, high-end, clean, simple, cohesive with my brand. Please refer my brand board. Business name color will be metallic bronzy color. Im thinking grey background or white background. Thanks

Target Market(s)

25-35. Gender neutral. People who are in Entertainment business industry.
This is High-end Eyelash extension salon in Beverly Hills

Industry/Entity Type

Beauty Salon

Contact Information for Business Card

Business name: Lumarra
Name of person: will provide later
Address 6128 N.Corbel Ridge Blvd Beverly Hills , CA 90210
Phone: will provide later (Text only)
Web: www.lumarrastudio-example.com
Pictogrid icon, Friendvale icon
follow us for seasonal campaign and news @lumarrastudioexample

Requirements
Must have
• Beautiful, elegant, clean and simple look but very attractive and modern
Should not have
• We don't like too clutter, too busy designs.

```html
<!DOCTYPE html>
<html lang="en">
<head>
<meta charset="utf-8">
<title>Lumarra — Business Card</title>
<link rel="stylesheet" href="https://fonts.googleapis.com/css2?family=Playfair+Display:wght@400&family=Montserrat:wght@400&display=swap">
<style>
  :root {
    --backdrop: #2b2b2b;
    --backdrop-edge: #1a1a1a;
    --card: #1d1d1d;
    --ink: #f2f2f2;
    --logo: #cfcfcf;
    --muted: #bdbdbd;
  }
  * { box-sizing: border-box; margin: 0; padding: 0; }
  html, body { width: 1200px; height: 900px; overflow: hidden; }
  body {
    position: relative;
    background: radial-gradient(ellipse at 70% 20%, var(--backdrop) 0%, var(--backdrop-edge) 100%);
    font-family: "Playfair Display", Georgia, serif;
    color: var(--ink);
  }
  .card {
    position: absolute;
    background: var(--card);
    box-shadow: 0 14px 34px rgba(0,0,0,.55);
  }
  .card--front { left: 400px; top: 40px; width: 610px; height: 348px; }
  .card--back  { left: 215px; top: 420px; width: 770px; height: 440px; }

  .wordmark { position: absolute; text-align: right; }
  .wordmark__name {
    font-family: "Playfair Display", Georgia, serif;
    font-weight: 400;
    color: var(--logo);
    line-height: 1;
    letter-spacing: 1px;
  }
  .wordmark__place {
    font-family: "Montserrat", Arial, sans-serif;
    color: var(--muted);
    letter-spacing: 3px;
    margin-top: 10px;
  }
  .card--front .wordmark { right: 70px; top: 120px; }
  .card--front .wordmark__name { font-size: 84px; }
  .card--front .wordmark__place { font-size: 12px; }
  .card--back .wordmark { left: 40px; top: 50px; }
  .card--back .wordmark__name { font-size: 78px; }
  .card--back .wordmark__place { font-size: 11px; }

  .person { position: absolute; right: 44px; top: 250px; text-align: right; }
  .person__name { font-size: 30px; letter-spacing: .5px; }
  .person__role { font-size: 12px; color: var(--muted); }

  .contact {
    position: absolute; right: 44px; top: 318px; text-align: right;
    font-size: 17px; line-height: 24px; letter-spacing: 1.2px;
  }
  .social {
    position: absolute; left: 40px; top: 366px;
    display: flex; align-items: center; gap: 10px;
    font-size: 15px; letter-spacing: 1px;
  }
  .social__mark { width: 10px; height: 10px; border-radius: 50%; background: var(--ink); }
  .social__names { color: var(--muted); font-size: 13px; }
</style>
</head>
<body>
  <section class="card card--front">
    <div class="wordmark">
      <div class="wordmark__name">Lumarra</div>
      <div class="wordmark__place">BEVERLY HILLS</div>
    </div>
  </section>

  <section class="card card--back">
    <div class="wordmark">
      <div class="wordmark__name">Lumarra</div>
      <div class="wordmark__place">BEVERLY HILLS</div>
    </div>

    <div class="person">
      <div class="person__name">Camille Arden</div>
      <div class="person__role">CEO | Founder</div>
    </div>

    <address class="contact" style="font-style:normal">
      info@lumarrastudio-example.com<br>
      021 555 0186<br>
      www.lumarrastudio-example.com<br>
      6128 N.Corbel Ridge Blvd Beverly Hills , CA 90210
    </address>

    <div class="social">
      <span class="social__mark"></span>
      <span class="social__names">Pictogrid · Friendvale</span>
      <span class="social__handle">@lumarrastudioexample</span>
    </div>
  </section>
</body>
</html>
```